Vosk and Telby Website

Vosk & Telby Website

The purpose of the Vosk & Telby website has 2 purposes; number 1 is to SALE the most “Rugged and Reliable products with the most versatile innovation possible. Number 2 to attract and assist territory sales manager across the United States with an easy flow website and customer sales support in the background.

Our Website Vision

This Website should be very modern and professional with a easy flow, we will use the following platform and plug-ins built with then website builder Divi Word press with Woo commerce with a sales professional CRM ( submit the plug-in of your choice for review before adding to programming) in the backend. We will provide information to the look we are looking for. All background images will be Black and White. We will provide professional images of our products that have been trimmed out and saved with a transparent background so that they can be added to a custom designed background or black and white image that will enhance the product. I want all the special tools provided in the Divi Family of tools used to give this website the WOW FACTOR. As of Now or site will be hosted on Plume Vault

Header design should have a Center VT Logo provided with a Hamburger Menu on the left and on the right a Search Glass Icon a Person Icon for login and register and Sales Cart Icon this could in the only Page that is Full Page Black and White image that can be blurred or ghosted back as we want the main page to be a line of 6 to 8 different Carts and Dollies to represent our products in color. Designer can take the images of our product and color correct Photoshop or whatever is needed to make it look its best. That is the landing or main image. The home page will be a slider of up to five images with 4 major messages to our customer or reasons to do business with Vosk & Telby. I will download 2 image to give you a idea of direction.

Slider Messages: Price Match Guarantee
Industry Best Warranty 5 Years on Frame 3 Years on Casters
Customize to fit your Surface and Application
Designed, Engineered and Manufactured Proudly in the U.S.A.

Categories/ Products Page
Carts
Dollies
Casters
Used Equipment

Categories Page

Products Page
Ratings with stars and comments
WooCommerce Composite products

Customization Page

Career Page

Contact page

Policy Page

Terms and Conditions Page

LOOK AT ZELMIRAB7BAY.COM WEBSITE MUST BE BETTER

Target Market(s)

We are a manufacturer of the worlds most rugged and reliable Industrial carts, dollies, hand trucks and casters. we will be selling to all types of industry's from distributors warehouse hospitals

Industry/Entity Type

Light Industrial

Coding

Coded - Design and coding required

Number of Pages Required

5+ page

Colors
ec1f27

Requirements
Must have
• Monochrome with Products colored and buttons and logo color codes in logo are Red # AF002A and Gray #5B5C5E
• Divi we own a lifetime license
• WordPress
• Woocommerce
• woocommerce composite products
• WP forms
• CRM
• Welder image is meant to be used Customization Page
Nice to have
• CRM for our 100 plus reps

```html
<!DOCTYPE html>
<html lang="en">
<head>
<meta charset="utf-8">
<title>Vosk &amp; Telby — Rugged and Reliable Versatile Innovation</title>
<link rel="stylesheet" href="https://fonts.googleapis.com/css2?family=Russo+One&family=Open+Sans:wght@400;600;700&display=swap">
<style>
:root{
  --red:#d81e46;
  --red-deep:#af002a;
  --ink:#111111;
  --text:#555;
  --grey:#5b5c5e;
  --band:#ededed;
  --footer:#1b1b1d;
  --faint:#f7dbe2;
  --white:#fff;
}
*{box-sizing:border-box;margin:0;padding:0}
html,body{width:1200px;height:4011px;overflow:hidden;background:var(--white)}
body{position:relative;font-family:'Open Sans',sans-serif;color:var(--text)}
.abs{position:absolute}
.display{font-family:'Russo One',sans-serif;color:var(--ink);text-transform:uppercase;letter-spacing:1px}
.underline{display:flex;gap:8px;justify-content:center;margin-top:6px}
.underline i{display:block;height:3px;background:var(--red)}
.underline i:nth-child(1){width:70px}.underline i:nth-child(2){width:44px}.underline i:nth-child(3){width:8px}
.ghost-word{font-family:'Russo One',sans-serif;color:var(--faint);font-size:72px;text-transform:uppercase;line-height:1;letter-spacing:2px}
.btn-outline{border:2px solid #222;font-family:'Russo One',sans-serif;font-size:13px;color:#111;display:flex;align-items:center;justify-content:center;background:#fff;text-transform:uppercase}

/* header + hero */
.hero{left:0;top:0;width:1200px;height:600px;background:radial-gradient(ellipse at 60% 60%,#6a6a6a 0%,#2a2a2a 40%,#050505 80%)}
.brand{display:flex;align-items:center;gap:10px}
.brand-mark{width:40px;height:40px;background:var(--red)}
.brand-name{font-family:'Russo One',sans-serif;font-size:26px;color:#fff;line-height:1}
.brand-tag{font-size:7.5px;color:#fff;letter-spacing:1px;text-transform:uppercase;margin-top:3px}
.nav{left:510px;top:28px;display:flex;gap:0;align-items:center;font-size:12.5px;color:#fff}
.nav a{color:#fff;text-decoration:none;padding:4px 9px;margin-right:24px}
.nav a.active{background:#fff;color:var(--red)}
.search{left:967px;top:29px}
.login{left:1028px;top:22px;width:128px;height:38px;background:#fff;color:var(--red);font-size:13px;font-weight:700;display:flex;align-items:center;justify-content:center}
.hero-title{left:0;top:214px;width:1200px;text-align:center;font-size:52px;color:#fff}
.hero-copy{left:360px;top:284px;width:480px;text-align:center;color:#fff;font-size:13.5px;line-height:21px}
.buy{left:512px;top:378px;width:174px;height:50px;background:var(--red);display:flex;align-items:center;padding-left:16px;font-family:'Russo One',sans-serif;color:#fff;font-size:18px}
.buy .cart{position:absolute;right:4px;top:4px;width:44px;height:42px;background:#fff;display:flex;align-items:center;justify-content:center}

/* about */
.about-title{left:0;top:672px;width:1200px;text-align:center;font-size:36px}
.about-copy{left:305px;top:740px;width:590px;text-align:center;font-size:12.5px;line-height:21px}
.feature{width:114px;height:116px;background:#fff;box-shadow:0 2px 10px rgba(0,0,0,.15);text-align:center;font-size:13px;font-weight:700;color:#222;line-height:16px;padding-top:14px}
.feature svg{display:block;margin:0 auto 6px}

/* section headers */
.banner-title{left:0;width:1200px;text-align:center;font-size:38px}

/* rugged */
.rugged-card{left:159px;top:1405px;width:452px;height:263px;background:#fff;box-shadow:0 2px 10px rgba(0,0,0,.12);padding:40px 34px 0 33px}
.rugged-card h3{font-family:'Russo One',sans-serif;font-size:20px;color:var(--red);text-transform:uppercase;font-weight:400}
.rugged-card p{font-size:12.5px;line-height:21px;margin-top:6px;width:390px}
.photo-frame{left:570px;top:1338px;width:470px;height:394px;background:#fff;box-shadow:0 2px 10px rgba(0,0,0,.15);padding:12px}
.photo{width:100%;height:100%}

/* categories */
.cat-band{left:0;top:1852px;width:1200px;height:1170px;background:linear-gradient(180deg,#eeeeee,#f3f3f3 60%,#e9e9e9)}
.red-block{background:var(--red)}
.white-card{background:#fff}
.used-title{font-family:'Russo One',sans-serif;font-size:18px;color:#111;text-transform:uppercase}
.price{color:var(--red);font-weight:700;font-size:14px}

/* testimonials */
.t-card{width:241px;height:194px;background:#fff;box-shadow:0 2px 10px rgba(0,0,0,.15);padding:16px 14px;font-size:11.5px;line-height:21px;color:#777}
.t-client{display:flex;align-items:center;gap:10px;margin-top:6px}
.avatar{width:46px;height:46px;border-radius:50%;background:linear-gradient(180deg,#9fb3c8,#34465e)}
.t-name{color:var(--red);font-weight:700;font-size:13px;line-height:16px}
.stars{color:#d98a00;font-size:12px;line-height:14px;letter-spacing:1px}
.dot{width:12px;height:12px;border-radius:50%;background:#555}

/* footer */
.footer{left:0;top:3690px;width:1200px;height:321px;background:var(--footer)}
.footer-copy{left:360px;top:3814px;width:480px;text-align:center;color:#fff;font-size:12px;line-height:21px}
.social{top:3879px;width:36px;height:36px;background:var(--red)}
.rule{left:159px;top:3955px;width:880px;height:1px;background:#444}
.legal{left:0;top:3974px;width:1200px;text-align:center;color:#fff;font-size:11.5px}
</style>
</head>
<body>

<!-- HERO -->
<section class="abs hero" role="img" aria-label="Black and white photo of welding sparks in a workshop"></section>
<div class="abs brand" style="left:162px;top:22px">
  <span class="brand-mark"></span>
  <div><div class="brand-name">VOSK &amp; TELBY</div><div class="brand-tag">Rugged and Reliable Versatile Innovation</div></div>
</div>
<nav class="abs nav">
  <a>Home</a><a class="active">About Us</a><a>Category</a><a>Testimonials</a><a>Contact Us</a>
</nav>
<svg class="abs search" width="26" height="26" viewBox="0 0 26 26"><circle cx="13" cy="13" r="11.5" fill="none" stroke="#d81e46" stroke-width="1.6"/><circle cx="12" cy="12" r="4" fill="none" stroke="#d81e46" stroke-width="1.6"/><line x1="15" y1="15" x2="18" y2="18" stroke="#d81e46" stroke-width="1.6"/></svg>
<div class="abs login">Login / Register</div>
<div class="abs hero-title display">Price Match Guarantee</div>
<p class="abs hero-copy">Industry Best Warranty 5 Years on Frame 3 Years on Casters Customize to fit your Surface and Application , Designed, Engineered and Manufactured Proudly in the U.S.A.</p>
<div class="abs buy">BUY NOW
  <span class="cart"><svg width="26" height="22" viewBox="0 0 26 22"><path d="M1 2h4l3 12h13l3-9H7" fill="none" stroke="#d81e46" stroke-width="2.2"/><circle cx="10" cy="18.5" r="2" fill="#d81e46"/><circle cx="19" cy="18.5" r="2" fill="#d81e46"/></svg></span>
</div>

<!-- ABOUT -->
<svg class="abs" style="left:0;top:840px" width="131" height="262" role="img" aria-label="Red-toned photo of a factory floor in a diamond shape"><defs><linearGradient id="gl" x1="0" y1="0" x2="1" y2="1"><stop offset="0" stop-color="#a8112e"/><stop offset="1" stop-color="#e45270"/></linearGradient></defs><polygon points="0,0 131,131 0,262" fill="url(#gl)"/></svg>
<svg class="abs" style="left:1067px;top:685px" width="133" height="267" role="img" aria-label="Red-toned photo of a warehouse interior in a diamond shape"><defs><linearGradient id="gr" x1="0" y1="0" x2="1" y2="1"><stop offset="0" stop-color="#e97a93"/><stop offset="1" stop-color="#c21d44"/></linearGradient></defs><polygon points="133,0 0,133 133,267" fill="url(#gr)"/></svg>
<div class="abs ghost-word" style="left:996px;top:998px">CART</div>

<div class="abs about-title display">About Us<div class="underline"><i></i><i></i><i></i></div></div>
<p class="abs about-copy">Lorem Ipsum is simply dummy text of the printing and typesetting industry. Lorem Ipsum has been the industry's standard dummy text ever since the 1500s, when an unknown printer took a galley of type and scrambled it to make a type specimen book. It has survived not only five centuries, but also the leap into electronic typesetting, remaining essentially unchanged.</p>
<div class="abs feature" style="left:467px;top:857px">
  <svg width="46" height="46" viewBox="0 0 46 46"><circle cx="23" cy="23" r="20" fill="none" stroke="#d81e46" stroke-width="2" stroke-dasharray="5 2"/><circle cx="23" cy="23" r="12" fill="none" stroke="#d81e46" stroke-width="2"/><path d="M17 23l4 4 8-8" fill="none" stroke="#d81e46" stroke-width="2"/></svg>
  5 Year<br>Warranty
</div>
<div class="abs feature" style="left:616px;top:857px">
  <svg width="46" height="46" viewBox="0 0 46 46"><circle cx="23" cy="23" r="20" fill="none" stroke="#d81e46" stroke-width="2"/><rect x="16" y="13" width="14" height="19" rx="2" fill="none" stroke="#d81e46" stroke-width="2"/><line x1="19" y1="19" x2="27" y2="19" stroke="#d81e46" stroke-width="2"/><line x1="19" y1="24" x2="25" y2="24" stroke="#d81e46" stroke-width="2"/></svg>
  3 Year Frame<br>Casters
</div>
<div class="abs btn-outline" style="left:538px;top:1027px;width:122px;height:41px">Read More</div>

<!-- VERSATILE INNOVATION -->
<svg class="abs" style="left:358px;top:1164px" width="484" height="131"><line x1="0" y1="20" x2="484" y2="20" stroke="#d81e46" stroke-width="2"/><polygon points="104,0 378,0 240,131" fill="#d81e46"/></svg>
<div class="abs banner-title display" style="top:1206px">Versatile Innovation<div class="underline"><i></i><i></i><i></i></div></div>

<svg class="abs" style="left:104px;top:1350px" width="170" height="145"><defs><pattern id="dots" width="22" height="22" patternUnits="userSpaceOnUse"><circle cx="2" cy="2" r="1.6" fill="#c8c8c8"/></pattern></defs><rect width="170" height="145" fill="url(#dots)"/></svg>
<div class="abs rugged-card">
  <h3>Rugged and Reliable Products</h3>
  <p>Lorem Ipsum is simply dummy text of the printing and typesetting industry. Lorem Ipsum has been the industry's standard dummy text ever since the 1500s, when an unknown printer took a galley of type and scrambled it to make a type specimen book.</p>
  <div class="btn-outline" style="width:150px;height:41px;margin-top:24px">Explore More</div>
</div>
<div class="abs photo-frame"><div class="photo" role="img" aria-label="Photo of a welder in red protective gear working on a steel frame" style="background:linear-gradient(120deg,#2a0d0a 0%,#8a1d17 35%,#3b1712 60%,#6c5a8a 80%,#1a0c08 100%)"></div></div>
<div class="abs ghost-word" style="left:5px;top:1708px">INNOVATION</div>

<!-- CATEGORIES -->
<section class="abs cat-band" role="img" aria-label="Faded black and white photo of sparks in a workshop"></section>
<div class="abs display" style="left:162px;top:1922px;font-size:34px">Categories<div class="underline" style="justify-content:flex-start"><i></i><i></i><i></i></div></div>
<svg class="abs" style="left:912px;top:1912px" width="170" height="110"><rect width="170" height="110" fill="url(#dots)"/></svg>

<div class="abs red-block" style="left:663px;top:1953px;width:375px;height:269px"></div>
<div class="abs white-card" style="left:604px;top:1976px;width:412px;height:223px;padding:18px 50px"><div role="img" aria-label="Blue flatbed platform dolly" style="width:100%;height:100%;background:radial-gradient(ellipse at 50% 55%,#1d5a8c 0%,#174a74 40%,#fff 72%)"></div></div>
<div class="abs ghost-word" style="left:401px;top:1972px;color:#ebbfcb">DOLLIES</div>

<div class="abs ghost-word" style="left:162px;top:2052px;color:#ebbfcb;text-transform:none;font-family:'Open Sans',sans-serif;font-weight:700;font-size:68px">Casters</div>
<svg class="abs" style="left:118px;top:2080px" width="40" height="150"><rect width="40" height="150" fill="url(#dots)"/></svg>
<div class="abs red-block" style="left:184px;top:2124px;width:224px;height:381px"></div>
<div class="abs white-card" style="left:162px;top:2148px;width:269px;height:334px;padding:20px 50px"><div role="img" aria-label="Teal convertible hand truck with forks" style="width:100%;height:100%;background:radial-gradient(ellipse at 45% 50%,#2a8fa8 0%,#2a8fa8 18%,#fff 55%)"></div></div>

<svg class="abs" style="left:600px;top:2380px" width="110" height="240"><rect width="110" height="240" fill="url(#dots)"/></svg>
<div class="abs red-block" style="left:641px;top:2303px;width:269px;height:266px"></div>
<div class="abs white-card" style="left:663px;top:2276px;width:225px;height:317px;padding:20px 40px"><div role="img" aria-label="Aluminium hand truck" style="width:100%;height:100%;background:radial-gradient(ellipse at 50% 50%,#b8b8b8 0%,#d0d0d0 20%,#fff 55%)"></div></div>
<div class="abs ghost-word" style="left:727px;top:2622px;color:#ebbfcb">CARTS</div>

<svg class="abs" style="left:312px;top:2830px" width="170" height="150"><rect width="170" height="150" fill="url(#dots)"/></svg>
<div class="abs red-block" style="left:349px;top:2670px;width:375px;height:270px"></div>
<div class="abs white-card" style="left:370px;top:2694px;width:452px;height:224px"></div>
<div class="abs" role="img" aria-label="Red two-shelf utility cart" style="left:388px;top:2706px;width:172px;height:200px;background:radial-gradient(ellipse at 50% 55%,#c8202a 0%,#d63a44 22%,#fff 60%)"></div>
<div class="abs" style="left:585px;top:2720px;width:225px">
  <div class="used-title">Used Equipment</div>
  <div class="price" style="margin-top:6px">$ 50.55</div>
  <p style="font-size:11px;line-height:20px;margin-top:2px">Lorem Ipsum is simply dummy text of the printing and typesetting industry. Lorem Ipsum has been the industry.</p>
</div>
<div class="abs btn-outline" style="left:585px;top:2843px;width:112px;height:40px">Buy Now</div>

<!-- TESTIMONIALS -->
<svg class="abs" style="left:358px;top:3128px" width="484" height="131"><line x1="0" y1="20" x2="484" y2="20" stroke="#d81e46" stroke-width="2"/><polygon points="104,0 378,0 240,131" fill="#d81e46"/></svg>
<div class="abs banner-title display" style="top:3170px">Testimonials<div class="underline"><i></i><i></i><i></i></div></div>

<div class="abs t-card" style="left:216px;top:3307px">Lorem Ipsum is simply dummy text of the printing and typesetting industry. Lorem Ipsum has been the industry's standard dummy text ever since the 1500s,
  <div class="t-client"><span class="avatar" role="img" aria-label="Client portrait"></span><div><div class="t-name">- Client Name</div><div class="stars">★★★★☆</div></div></div></div>
<div class="abs t-card" style="left:479px;top:3307px">Lorem Ipsum is simply dummy text of the printing and typesetting industry. Lorem Ipsum has been the industry's standard dummy text ever since the 1500s,
  <div class="t-client"><span class="avatar" role="img" aria-label="Client portrait"></span><div><div class="t-name">- Client Name</div><div class="stars">★★★★☆</div></div></div></div>
<div class="abs t-card" style="left:741px;top:3307px">Lorem Ipsum is simply dummy text of the printing and typesetting industry. Lorem Ipsum has been the industry's standard dummy text ever since the 1500s,
  <div class="t-client"><span class="avatar" role="img" aria-label="Client portrait"></span><div><div class="t-name">- Client Name</div><div class="stars">★★★★☆</div></div></div></div>

<span class="abs dot" style="left:545px;top:3558px;background:var(--red)"></span>
<span class="abs dot" style="left:593px;top:3558px"></span>
<span class="abs dot" style="left:643px;top:3558px"></span>
<div class="abs ghost-word" style="left:848px;top:3548px;font-size:68px">REVIEWS</div>

<!-- FOOTER -->
<footer class="abs footer"></footer>
<svg class="abs" style="left:358px;top:3690px" width="484" height="70"><line x1="0" y1="14" x2="484" y2="14" stroke="#d81e46" stroke-width="2"/><polygon points="104,0 378,0 240,70" fill="#d81e46"/></svg>
<div class="abs brand" style="left:437px;top:3738px">
  <span class="brand-mark"></span>
  <div><div class="brand-name" style="font-size:27px">VOSK &amp; TELBY</div><div class="brand-tag">Rugged and Reliable Versatile Innovation</div></div>
</div>
<p class="abs footer-copy">Lorem Ipsum is simply dummy text of the printing and typesetting industry. Lorem Ipsum has been the industry's standard dummy text ever since the 1500s,</p>
<span class="abs social" style="left:514px" aria-label="Social link"></span>
<span class="abs social" style="left:559px" aria-label="Social link"></span>
<span class="abs social" style="left:604px" aria-label="Social link"></span>
<span class="abs social" style="left:649px" aria-label="Social link"></span>
<div class="abs rule"></div>
<p class="abs legal">Copyright © 2019. Vosk &amp; Telby. All Rights Reserved. Terms &amp; Conditions | Privacy Policy.</p>

</body>
</html>
```